Brevard médico-conseils - word template

We are dooing lot of médical report from word document. We dont print the text on a stationnary. We are producting the report and save it in pdf. So I need à word template. I want something more than just hard the logo. I would like the look of a stationnary in the word template.

I put an exemple of report. But the final don't have to look that way. Propose something more acurate.
After that I will need a business card.

Industry/Entity Type

Medical

Requirements
Must have
• We have to do a design that integrate are logo and color. You have the file in the project.
• The wrihting beteen the title must be in times new roman.
Nice to have
• We have 2 offices:
• Québec (Building Val-Doré) 512, ave des Tilleuls, local 210, G2K 4P7 T.418 555-7142 T.418 555-7189
• St-Romuald (Building Carrefour Marbel-Les quais) 2350, boul. des Érables, local 305, G7B 2N4. T.418 555-0263 F.418 555-0398
• Mail: info@BrevardMC.com and expertise@BrevardMC.com
• Web: www.BrevardMC.com
• For now you can type www.PTRV.ca to acces the web site.
Should not have
• The same look that the exemple. Because I want to upgrade the look of the company.

```html
<!DOCTYPE html>
<html lang="fr">
<head>
<meta charset="utf-8">
<title>Brevard médico-conseils — Rapport complémentaire du médecin</title>
<link rel="stylesheet" href="https://fonts.googleapis.com/css2?family=Open+Sans:ital,wght@0,400;0,600;0,700;1,400&display=swap">
<style>
  :root{
    --bg:#ebebeb;
    --paper:#ffffff;
    --teal:#7fc4b8;
    --grey-band:#c9c9c9;
    --ink:#111111;
    --logo-grey:#555555;
    --muted:#333333;
  }
  *{margin:0;padding:0;box-sizing:border-box}
  html,body{width:1200px;height:1000px;overflow:hidden;background:var(--bg)}
  body{font-family:"Open Sans",Arial,sans-serif;color:var(--ink);position:relative}
  .page{position:absolute;left:340px;top:58px;width:575px;height:814px;background:var(--paper)}
  .band-teal{position:absolute;left:0;top:0;width:37px;height:100%;background:var(--teal)}
  .band-grey{position:absolute;left:41px;top:0;width:10px;height:100%;background:var(--grey-band)}
  .abs{position:absolute;white-space:nowrap}
  .brand{left:77px;top:38px;display:flex;align-items:center;gap:8px;font-size:21px;font-weight:600;color:var(--logo-grey);letter-spacing:-.2px}
  .brand-square{width:28px;height:28px;background:var(--logo-grey)}
  .services{left:383px;top:41px;font-size:11px;line-height:14px;color:var(--muted)}
  .title{left:0;width:100%;top:122px;text-align:center;font-size:11px;font-weight:700;letter-spacing:.2px}
  .section-bar{position:absolute;left:115px;width:387px;height:22px;background:var(--teal);color:#fff;font-size:11.5px;font-weight:600;padding:3px 8px}
  .t{position:absolute;white-space:nowrap;font-size:10px;line-height:12px}
  .lbl{font-weight:700}
  .b{font-weight:700}
  .dot{display:inline-block;width:5px;height:5px;border-radius:50%;background:var(--ink);margin-right:5px;vertical-align:1px}
  .note{font-style:italic;text-decoration:underline;font-size:9.5px}
  .footer-mark{position:absolute;left:76px;top:760px;width:4px;height:22px;background:var(--teal)}
  .foot{position:absolute;left:89px;font-size:6.6px;line-height:9px;white-space:nowrap;color:var(--ink)}
  .foot svg{width:7px;height:7px;vertical-align:-1px;margin:0 2px}
</style>
</head>
<body>
<main class="page">
  <div class="band-teal"></div>
  <div class="band-grey"></div>

  <header>
    <div class="abs brand"><span class="brand-square"></span>Brevard médico-conseils</div>
    <div class="abs services">Expertise Service santé Pré-emploi<br>Bilan exécutif Vaccination</div>
  </header>

  <h1 class="abs title">RAPPORT COMPLÉMENTAIRE DU MÉDECIN</h1>

  <div class="section-bar" style="top:167px">Information</div>
  <div class="t lbl" style="left:123px;top:199px">NO. DE DOSSIER</div><div class="t" style="left:228px;top:199px">: #7101</div>
  <div class="t lbl" style="left:123px;top:211px">EMPLOYEUR</div><div class="t" style="left:228px;top:211px">: NORDELLE</div>
  <div class="t lbl" style="left:123px;top:222px">EMPLOYÉ(E)</div><div class="t" style="left:228px;top:222px">: toto</div>
  <div class="t lbl" style="left:123px;top:234px">POSTE</div><div class="t" style="left:228px;top:234px">: Marchandiseur</div>
  <div class="t lbl" style="left:123px;top:245px">DATE DE L’EXAMEN</div><div class="t" style="left:228px;top:245px">: 27/03/2015</div>

  <div class="section-bar" style="top:281px">Médical</div>
  <div class="t lbl" style="left:123px;top:313px">ANTÉCÉDENTS</div>
  <div class="t" style="left:227px;top:313px">:&nbsp;&nbsp;&nbsp;<span class="dot"></span>Poids fort</div>
  <div class="t" style="left:239px;top:324px"><span class="dot"></span>Allergies : Pénicilline</div>
  <div class="t" style="left:243px;top:347px"><span class="b">Symptômes :</span> Le candidat n’a pas identifié de symptôme.</div>
  <div class="t" style="left:243px;top:370px"><span class="b">Maladies</span>&nbsp;&nbsp;&nbsp;&nbsp;&nbsp; : Le candidat n’a JAMAIS manqué du travail</div>
  <div class="t" style="left:243px;top:382px">dû à l’une des maladies identifiées ici-bas.</div>
  <div class="t" style="left:251px;top:394px"><span class="dot"></span>Depuis novembre 2014 – tube oreille droite.</div>

  <div class="t lbl" style="left:123px;top:417px">EXAMEN PHYSIQUE</div>
  <div class="t" style="left:228px;top:417px">: Normal</div>
  <div class="t" style="left:233px;top:429px">SAUF&nbsp; : Excès de poids</div>

  <div class="t lbl" style="left:123px;top:452px">RECOMMANDATIONS</div>
  <div class="t" style="left:228px;top:452px">: Apte au travail</div>
  <div class="t" style="left:236px;top:464px"><span class="dot"></span>16 - Pas de bruits, protection exigée</div>

  <div class="t lbl" style="left:123px;top:487px">DOSSIER DE CSST</div>
  <div class="t" style="left:228px;top:487px">: Aucun</div>

  <div class="section-bar" style="top:528px">RX</div>
  <div class="t note" style="left:123px;top:560px">(Pour la description exacte – voir le rapport de radiologie)</div>
  <div class="t lbl" style="left:123px;top:583px">RX-LOMBAIRE PAS</div>
  <div class="t" style="left:228px;top:583px">: de restriction Léger pincement</div>

  <div class="t lbl" style="left:123px;top:636px">Médecin</div><div class="t" style="left:228px;top:636px">: Dr Louis Marchand</div>
  <div class="t lbl" style="left:123px;top:648px">Rédaction</div><div class="t" style="left:228px;top:648px">: Hélène Vasseur</div>
  <div class="t lbl" style="left:123px;top:659px">Validation</div><div class="t" style="left:228px;top:659px">: LDD</div>
  <div class="t" style="left:403px;top:659px">Date : 27/03/2015</div>

  <footer>
    <div class="footer-mark"></div>
    <div class="foot" style="top:758px"><b>QUÉBEC</b> (Building Val-Doré) 512, ave des Tilleuls, local 210, G2K 4P7 |
      <svg viewBox="0 0 10 10"><path d="M2 1l2 2-1 1.5c.7 1.3 1.5 2.1 2.5 2.5L7 6l2 2-1.5 1.5C4.5 9 1 5.5.5 2.5z" fill="#111"/></svg>418 555-7142 |
      <svg viewBox="0 0 10 10"><rect x="1" y="3" width="8" height="5" fill="#111"/><rect x="3" y="1" width="4" height="2" fill="#111"/></svg>418 555-7189</div>
    <div class="foot" style="top:774px"><b>ST-ROMUALD</b> (Building Carrefour Marbel-Les quais) 2350, boul. des Érables, local 305, G7B 2N4 |
      <svg viewBox="0 0 10 10"><path d="M2 1l2 2-1 1.5c.7 1.3 1.5 2.1 2.5 2.5L7 6l2 2-1.5 1.5C4.5 9 1 5.5.5 2.5z" fill="#111"/></svg>418 555-0263 |
      <svg viewBox="0 0 10 10"><rect x="1" y="3" width="8" height="5" fill="#111"/><rect x="3" y="1" width="4" height="2" fill="#111"/></svg>418 555-0398</div>
  </footer>
</main>
</body>
</html>
```